Holiday Light Door Hanger

I need a new doorhanger design for our Holiday Light Service. I have attached our last one (which we DO like), but need to have a two-sided design. I also will attach photos that can be used as well as a FAQ about the service.

```html
<!DOCTYPE html>
<html lang="en">
<head>
<meta charset="utf-8">
<title>Holiday Light Door Hanger</title>
<link rel="stylesheet" href="https://fonts.googleapis.com/css2?family=Playfair+Display:wght@500&family=Figtree:wght@400;500&display=swap">
<style>
  :root {
    --bg: #f1ebe4;
    --navy: #23204a;
    --navy-deep: #1d1b3d;
    --plum: #5a3450;
    --amber: #b5843f;
    --gold-text: #d8b576;
    --gold-light: #ecd6a4;
    --gold-mid: #dcbd7d;
    --gold-dark: #c99f55;
    --photo-blue: #4a4f95;
    --photo-rose: #b0607a;
    --photo-night: #24223a;
    --white: #ffffff;
    --ink: #25223f;
  }
  * { box-sizing: border-box; margin: 0; padding: 0; }
  html, body { width: 1200px; height: 899px; overflow: hidden; background: var(--bg); }
  .canvas { position: relative; width: 1200px; height: 899px; background: var(--bg); }

  .hanger {
    position: absolute;
    top: 66px;
    width: 309px;
    height: 769px;
    border-radius: 155px 155px 0 0;
    overflow: hidden;
  }
  .hanger--front { left: 257px; }
  .hanger--back { left: 634px; }

  .hanger__hole {
    position: absolute;
    left: 94px;
    top: 71px;
    width: 122px;
    height: 122px;
    border-radius: 50%;
    background: var(--bg);
    z-index: 3;
  }

  /* Front */
  .front__body {
    position: absolute;
    inset: 0 0 115px 0;
    background: linear-gradient(to bottom,
      var(--navy) 0%, var(--navy) 30%, #3a2a4c 48%, var(--plum) 60%, #8c5c45 75%, var(--amber) 100%);
  }
  .front__sparkle {
    position: absolute;
    left: 0; right: 0; bottom: 115px;
    height: 110px;
    background: radial-gradient(ellipse at 50% 100%, rgba(255,236,190,0.5), rgba(255,236,190,0) 70%);
  }
  .front__title {
    position: absolute;
    left: 0; right: 0;
    top: 205px;
    text-align: center;
    font-family: "Playfair Display", serif;
    font-weight: 500;
    color: var(--gold-text);
  }
  .front__title-small { display: block; font-size: 72px; line-height: 1; letter-spacing: -1px; }
  .front__title-large { display: block; font-size: 104px; line-height: 1; letter-spacing: -2px; margin-top: -4px; }
  .front__services {
    position: absolute;
    left: 0; right: 0;
    top: 395px;
    text-align: center;
    font-family: "Figtree", sans-serif;
    font-weight: 400;
    font-size: 42px;
    line-height: 43px;
    color: var(--white);
  }
  .front__cta {
    position: absolute;
    left: 0; right: 0; bottom: 0;
    height: 115px;
    background: linear-gradient(to bottom, var(--gold-mid), var(--gold-light));
    text-align: center;
    font-family: "Figtree", sans-serif;
    color: var(--ink);
    padding-top: 20px;
  }
  .front__cta-main { display: block; font-size: 33px; font-weight: 500; letter-spacing: 0.5px; line-height: 1.1; }
  .front__cta-sub { display: block; font-size: 25px; font-weight: 400; line-height: 1.2; margin-top: 2px; }

  /* Back */
  .back__lights {
    position: absolute;
    left: 0; right: 0; top: 0;
    height: 300px;
    background: linear-gradient(to bottom, var(--navy), var(--navy-deep));
  }
  .back__photo {
    position: absolute;
    left: 0; right: 0;
    top: 300px;
    bottom: 136px;
    background: linear-gradient(135deg, var(--photo-blue) 0%, var(--photo-rose) 55%, var(--photo-night) 100%);
  }
  .back__info {
    position: absolute;
    left: 0; right: 0; bottom: 0;
    height: 136px;
    background: linear-gradient(to bottom, var(--gold-dark), var(--gold-mid) 55%, var(--gold-light));
    padding: 30px 30px 0;
    text-align: center;
    font-family: "Figtree", sans-serif;
    font-size: 13.5px;
    line-height: 1.28;
    color: var(--ink);
  }
</style>
</head>
<body>
<main class="canvas">
  <section class="hanger hanger--front" aria-label="Door hanger front">
    <div class="front__body"></div>
    <div class="front__sparkle"></div>
    <div class="hanger__hole"></div>
    <h1 class="front__title">
      <span class="front__title-small">Holiday</span>
      <span class="front__title-large">Light</span>
    </h1>
    <p class="front__services">Installation<br>&amp; Takedown<br>Services</p>
    <div class="front__cta">
      <span class="front__cta-main">BOOK NOW</span>
      <span class="front__cta-sub">BEFORE SLOTS FILL!</span>
    </div>
  </section>

  <section class="hanger hanger--back" aria-label="Door hanger back">
    <div class="back__lights" role="img" aria-label="Illustration of strings of colourful holiday bulbs on a night sky"></div>
    <div class="back__photo" role="img" aria-label="Photo of a multi-storey corner building lit with red and blue holiday lights at night"></div>
    <div class="hanger__hole"></div>
    <p class="back__info">Tempor nostrud culpa pariatur ipsum irure sint esse aliquip incididunt. Officia duis pariatur aliqua incididunt exercitation ea eiusmod.</p>
  </section>
</main>
</body>
</html>
```